Postcard Design

I'm hosting a retreat in Tuscany tag line ideas for front: "nourish your soul with a taste of Tuscany" or "Savor the sweet life and Nourish your soul with a taste of Tuscany" here is the pertinent info- trip date: September 5-12, 2015 number:1.877.413.5928 e/m:Info@PiccoloSoleHavens.com Web address:www.PiccoloSoleHavens.com
What's included:
• 7 nights Accommodations in beautiful Villa
• All Meals and Snacks included
• Special Wine tasting Excursion in Chianti
• Guided Tour of Siena
• Hands on Cooking Class at the villa
• Yoga, Meditation walks, Journaling
Something like this should be on back lower right side: Spaces Limited Reserve Yours Today!
Other wording ideas for back: Renew your spirit in the quiet beauty of the Tuscan landscape (maybe above what's included)
This can be near the "spaces limited" =Invest in your health, spirit and well-being *airfare not included. See website for details
More ideas/maybe a better way to word all this??:
Welcome to "la dolce vita" (The sweet life)
Have you always wanted to travel to Italy? Want to experience the culture in a special way you couldn't enjoy as a typical tourist? This is the trip you've been waiting for. Life is too short to wait any longer!
Hosts show with pictures:
Lucy Jane Ferrandi woman w/dark hair headshot
Retreat host
Sharing her love of Italy's beautiful culture with you is her special gift
And
Megan Okabashi
Personal wellness consultant
Yoga, Meditation, Asana, Reiki, Pilates

I included a photo of the current postcard I made front & back. You can also visit my website to get an idea of my style. I'm hoping you can make me a postcard that's more tantalizing, and will get me some clients! I will include some extra photos and feel free to use your own stock images... anything to help! Feel free to change up wording to make it more appealing, welcoming and make people chose to go on retreat with me instead the hundreds of other retreats out there.
Thank you
Lucy Jane

```html
<!DOCTYPE html>
<html lang="en">
<head>
<meta charset="utf-8">
<title>Piccolo Sole Havens – Tuscany Retreat Postcard</title>
<link rel="stylesheet" href="https://fonts.googleapis.com/css2?family=Playball&family=Arimo:wght@400&display=swap">
<style>
  :root {
    --backdrop: #5e5e5e;
    --brown: #3f2314;
    --brown-dark: #2e170c;
    --orange: #f07318;
    --orange-deep: #c9530a;
    --orange-light: #f79a3a;
    --cream: #ffffff;
    --ink: #3a1e0f;
    --rule: #333333;
  }
  * { box-sizing: border-box; margin: 0; padding: 0; }
  html, body { width: 824px; height: 1200px; overflow: hidden; }
  body { background: var(--backdrop); position: relative; font-family: "Arimo", Arial, sans-serif; }

  .card { position: absolute; overflow: hidden; }
  .card-front { left: 38px; top: 50px; width: 740px; height: 530px; background: var(--brown); }
  .card-back { left: 38px; top: 598px; width: 735px; height: 530px; background: var(--cream); }
  .card svg.shapes { position: absolute; inset: 0; }

  .brand-name {
    position: absolute; left: 207px; width: 325px; top: 22px;
    text-align: center; font-family: "Playball", cursive; color: var(--ink);
    font-size: 44px; line-height: 48px;
  }
  .tagline {
    position: absolute; left: 0; right: 0; top: 452px; text-align: center;
    font-family: "Playball", cursive; color: var(--cream); font-size: 35px;
  }

  .offer { position: absolute; left: 45px; width: 367px; top: 0; color: var(--cream); }
  .offer-heading {
    margin-top: 28px; text-align: center; font-family: "Playball", cursive;
    color: var(--ink); font-size: 21px; line-height: 26px;
  }
  .offer-intro { margin: 12px 0 0 8px; font-size: 12.2px; line-height: 17px; width: 355px; }
  .inclusions { list-style: none; margin: 6px 0 0 8px; font-size: 12.2px; line-height: 17.3px; }
  .inclusions li::before { content: "•"; margin-right: 7px; }
  .fine-print { margin: 4px 0 0 8px; font-size: 12.2px; }
  .call-to-action {
    margin-top: 14px; text-align: center; font-family: "Playball", cursive;
    color: var(--ink); font-size: 19px;
  }
  .trip-date {
    position: absolute; left: 115px; top: 338px; width: 220px; height: 40px;
    text-align: center; font-family: "Playball", cursive; color: var(--cream);
  }
  .trip-date small { display: block; font-size: 13px; line-height: 14px; }
  .trip-date span { display: block; font-size: 20px; line-height: 22px; }
  .contacts { position: absolute; top: 400px; left: 0; right: 0; text-align: center; list-style: none; font-size: 12.2px; line-height: 17.5px; }
  .contacts svg { width: 9px; height: 9px; vertical-align: -1px; margin-right: 4px; fill: var(--cream); }

  .stamp-box { position: absolute; left: 649px; top: 82px; width: 51px; height: 57px; border: 1px solid var(--rule); }
  .address-line { position: absolute; left: 492px; width: 205px; border-top: 1px solid var(--rule); }
</style>
</head>
<body>

<section class="card card-front">
  <svg class="shapes" width="740" height="530" viewBox="0 0 740 530">
    <defs>
      <linearGradient id="landscape" x1="0" y1="0" x2="0" y2="1">
        <stop offset="0" stop-color="#bcd8ee"/>
        <stop offset="0.3" stop-color="#5b7a2c"/>
        <stop offset="0.55" stop-color="#b7994f"/>
        <stop offset="1" stop-color="#6a8a33"/>
      </linearGradient>
      <linearGradient id="bannerFill" x1="0" y1="0" x2="1" y2="0">
        <stop offset="0" stop-color="#d85f0d"/>
        <stop offset="0.5" stop-color="#f58426"/>
        <stop offset="1" stop-color="#d85f0d"/>
      </linearGradient>
    </defs>
    <path d="M0,70 Q110,60 210,78 L530,78 Q630,60 740,70 L740,98 Q630,82 530,100 L210,100 Q110,82 0,98 Z" fill="var(--orange)"/>
    <path d="M0,95 Q110,80 210,98 L530,98 Q630,80 740,92 L740,385 Q560,365 370,395 Q180,365 0,388 Z"
          fill="url(#landscape)" role="img" aria-label="Photo of a Tuscan stone villa with a pool, cypress trees and golden rolling hills"/>
    <path d="M0,383 Q180,360 370,390 Q560,360 740,380 L740,428 Q560,390 370,420 Q180,390 0,428 Z" fill="var(--orange)"/>
    <path d="M207,0 L532,0 L532,150 L380,150 L370,165 L360,150 L207,150 Z" fill="url(#bannerFill)"/>
    <path d="M217,0 L217,140 L360,140 L370,155 L380,140 L522,140 L522,0" fill="none" stroke="var(--brown)" stroke-width="1.5"/>
  </svg>
  <h1 class="brand-name">Piccolo Sole<br>Havens</h1>
  <p class="tagline">Nourish your Soul with a taste of Tuscany</p>
</section>

<section class="card card-back">
  <svg class="shapes" width="735" height="530" viewBox="0 0 735 530">
    <defs>
      <linearGradient id="panelFill" x1="0" y1="0" x2="1" y2="1">
        <stop offset="0" stop-color="var(--orange-deep)"/>
        <stop offset="0.45" stop-color="var(--orange)"/>
        <stop offset="1" stop-color="var(--orange-deep)"/>
      </linearGradient>
    </defs>
    <path d="M0,0 L447,0 L447,430 Q220,400 0,425 Z" fill="var(--brown)"/>
    <path d="M30,0 L427,0 L427,488 L238,488 L228,500 L218,488 L30,488 Z" fill="url(#panelFill)"/>
    <path d="M45,0 L45,478 L218,478 L228,490 L238,478 L412,478 L412,0" fill="none" stroke="var(--brown)" stroke-width="1.5"/>
    <path d="M95,345 L115,340 L115,376 L95,382 L103,362 Z" fill="var(--brown-dark)"/>
    <path d="M355,345 L335,340 L335,376 L355,382 L347,362 Z" fill="var(--brown-dark)"/>
    <rect x="115" y="338" width="220" height="40" fill="var(--brown)"/>
  </svg>

  <div class="offer">
    <h2 class="offer-heading">Renew your spirit in the quiet<br>beauty of the Tuscan landscape</h2>
    <p class="offer-intro">Have you always wanted to travel to Italy? Want to experience the culture in a special way you couldn't enjoy as a typical tourist? This is the trip you've been waiting for. Life is too short to wait any longer!</p>
    <ul class="inclusions">
      <li>7 nights Accommodations in beautiful Villa</li>
      <li>All Meals and Snacks included</li>
      <li>Special Wine tasting Excursion in Chianti</li>
      <li>Guided Tour of Siena</li>
      <li>Hands on Cooking Class at the villa</li>
      <li>Yoga, Meditation walks, Journaling</li>
    </ul>
    <p class="fine-print">*airfare not included. See website for details</p>
    <p class="call-to-action">Spaces Limited Reserve Yours Today!</p>
    <div class="trip-date" style="left:70px"><small>Trip date:</small><span>September 5-12, 2015</span></div>
    <ul class="contacts">
      <li><svg viewBox="0 0 10 10"><path d="M2,0 L4,2.5 L3,3.5 Q4.5,6 6.5,7 L7.5,6 L10,8 L8.5,10 Q3,9 0,1.5 Z"/></svg>1.877.413.5928</li>
      <li><svg viewBox="0 0 10 10"><path d="M0,2 L10,2 L10,8 L0,8 Z M0.5,2.5 L5,5.5 L9.5,2.5" stroke="#c9530a" stroke-width="0.8"/></svg>Info@PiccoloSoleHavens.com</li>
      <li><svg viewBox="0 0 10 10"><circle cx="5" cy="5" r="5"/></svg>www.PiccoloSoleHavens.com</li>
    </ul>
  </div>

  <div class="stamp-box"></div>
  <div class="address-line" style="top:274px"></div>
  <div class="address-line" style="top:308px"></div>
  <div class="address-line" style="top:343px"></div>
</section>

</body>
</html>
```